Flyer-Design für Immobilienpräsentation
Zielgruppe
Meine Firma heißt 'Die Raumglanz Idee' und ich bin Home Stagerin und Einrichtungsberaterin. Ich bereite Immobilien für den Verkauf vor (Immobilienpräsentation), dass heißt ich 'richte' die jeweilige Immobilie mit Möbeln so ein, dass der Interessent ein 'hier-will-ich-wohnen Gefühl' beim betreten der Räumlichkeiten bekommt. Er soll sich in die jeweilige Immobilie im besten Fall sofort verlieben. Eingerichtete Immobilien verkaufen sich schneller da der Kunde ein Gefühl bekommt wie die Proportionen in den jeweiligen Räumen sind und keine kahle und nichts Aussagende Immobilie sieht. Die Zielgruppe sind in erster Linie Makler, Investoren, Bauträger aber auch private Personen.
Aufgabenstellung
Als einfachste Vorgabe dient meine Homepage und ein DIN Format ja meine Visitenkarte ist Waagerecht und da ich viele große Bilder gerne hätte bietet sich DIN A5 oder A6 an finde ich. Entweder Zweibruch Fensterfalz (siehe Druckpilot) oder wenn du eine Idee hast wie man es noch besser darstellen kann oder was besse aussieht bin ich offen.
In diesem Stil sollte es sein, bzw gerne auch etwas hochwertiger. Es sollen viele Fotos von einer gestageden Immobilie zu sehen sein inklusive eines Vorher-Nachher Bildes. Zu diesem Vorher- Nachher Bild gerne: mit Home Staging 11 Kaufzusagen innerhalb 2 Tage, verkauft zum Wunschpreis; ohne Home Staging 3 Monate auf den Markt, 15 Besichtigungen und keine Kaufzusage.
Text würde ich mich mehr auf die Schlagwörter konzentrieren:
-Immobilie schneller, einfacher zum Wunschpreis an Wunschkäufer verkaufen
-Home Staging - Der Schlüssel zu Ihrem Erfolg
- Mit Home Staging die Immobilie erlebbar machen und aus Kaufinteressenten werden Käufer
- Ihre Immobilie wird mit mir zum Bestseller
- professionell ausgebildete Interior Designerin/ Visual Merchandiserin und Home Stagerin bin ich Ihre perfekte Ansprechpartnerin für das erfolgreiche in Szene setzen Ihrer Immobilie
-Der 1. Eindruck zählt, innerhalb von 30 Sekunden entscheidet der Interessent unterbewusst ob Ihm die Immobilie gefällt.
Auf der letzen Seite gerne Kontakt, Foto von mir und das ich Verbandsmitglied der BVRI bin inklusive Logo und Handlungsaufforderung...irgendwie 'gehen sie den nächsten Schritt mit mir' oder 'lassen Sie uns den nächsten Schritt gemeinsam gehen'

```html
<!DOCTYPE html>
<html lang="de">
<head>
<meta charset="utf-8">
<title>Die Raumglanz Idee – Home Staging Flyer</title>
<link href="https://fonts.googleapis.com/css2?family=Fira+Sans+Condensed:wght@500;600&family=Open+Sans:wght@300;400;600&display=swap" rel="stylesheet">
<style>
  :root{
    --teal:#7fb5ab;
    --teal-dark:#5f9a90;
    --teal-line:#8cc0b6;
    --paper:#ffffff;
    --paper-grey:#efefef;
    --panel-grey:#e2e2e2;
    --ink:#4a4a4a;
    --ink-soft:#6d6d6d;
    --backdrop:#d6d3cf;
  }
  *{box-sizing:border-box;margin:0;padding:0}
  html,body{width:1200px;height:960px;overflow:hidden}
  body{background:var(--backdrop);font-family:"Open Sans",sans-serif;color:var(--ink);position:relative}
  .spread{position:absolute;left:150px;width:900px;height:440px;background:var(--paper);box-shadow:0 6px 18px rgba(0,0,0,.18);overflow:hidden}
  .spread--outside{top:30px}
  .spread--inside{top:495px}
  .abs{position:absolute}
  .photo{position:absolute}
  .panel-grey{position:absolute;background:var(--paper-grey)}
  .heading{font-family:"Fira Sans Condensed",sans-serif;font-weight:600;letter-spacing:.5px;text-transform:uppercase}
  .line{position:absolute;background:var(--teal-line)}
  .line--dark{background:#5b6b68}

  /* outside – left panel */
  .impression-box{left:22px;top:25px;width:272px;height:395px;background:var(--teal)}
  .impression-card{left:30px;top:35px;width:148px;height:312px;background:var(--paper);padding:10px 10px;border:1px solid #e5e5e5}
  .impression-card h3{font-size:9.5px;letter-spacing:.2px;white-space:nowrap;color:#3d3d3d;margin-bottom:9px}
  .impression-card p{font-size:6.3px;line-height:1.4;color:var(--ink-soft);margin-bottom:7px}
  .stats{left:196px;top:232px;color:#fff}
  .stat{margin-bottom:12px}
  .stat__value{font-family:"Fira Sans Condensed",sans-serif;font-weight:500;font-size:19px;line-height:1}
  .stat__label{font-size:9px;line-height:1.25;text-transform:uppercase;font-weight:300;letter-spacing:.3px}

  /* outside – middle panel */
  .brand-box{background:var(--paper);display:flex;align-items:center;justify-content:center;text-align:center;padding:6px;font-family:"Open Sans",sans-serif;font-weight:400;color:var(--teal-dark);letter-spacing:1.5px;text-transform:uppercase;line-height:1.5}
  .greeting{left:432px;top:190px;width:168px;height:60px;background:var(--teal);color:#fff;font-size:8.5px;font-weight:300;padding:13px 12px;line-height:1.35}
  .contact{left:432px;top:282px;font-size:7.2px;line-height:1.35;color:var(--ink)}
  .contact strong{font-size:9px;font-weight:600;display:block}
  .contact p{margin-bottom:8px}

  /* outside – cover */
  .cover-band{left:600px;top:198px;width:300px;height:58px;background:var(--teal);color:#fff;text-align:center;padding-top:4px}
  .cover-band .heading{font-size:27px;line-height:1.1}
  .cover-band .sub{font-size:13px;font-weight:300}

  /* inside */
  .hero-title{left:52px;top:28px;color:#fff}
  .hero-title .heading{font-size:33px;text-shadow:0 1px 2px rgba(0,0,0,.15)}
  .hero-title .sub{font-size:22px;font-weight:300;line-height:1.2;margin-top:10px}
  .definition{left:30px;top:278px;width:156px;height:142px;background:var(--teal);color:#fff;padding:10px 10px}
  .definition h3{font-size:11px;margin-bottom:9px}
  .definition p{font-size:6.5px;line-height:1.4;font-weight:300;margin-bottom:7px}
  .bestseller{left:330px;top:55px;width:152px;height:165px;background:var(--teal);color:#fff;padding:10px 10px}
  .bestseller h3{font-size:10px;line-height:1.25;margin-bottom:9px}
  .bestseller p{font-size:6.5px;line-height:1.4;font-weight:300;margin-bottom:7px}
  .nametag{left:512px;top:202px;width:88px;height:24px;background:var(--teal);color:#fff;font-size:8.5px;white-space:nowrap;display:flex;align-items:center;justify-content:center;z-index:2}
  .compare{position:absolute;padding:10px 26px 10px 12px;z-index:2}
  .compare h4{font-family:"Open Sans",sans-serif;font-weight:300;font-size:19px;letter-spacing:.5px;margin-bottom:6px}
  .compare p{font-size:7px;line-height:1.3}
  .compare--before{left:600px;top:30px;width:145px;height:88px;background:var(--panel-grey);color:var(--ink-soft);clip-path:polygon(0 0,84% 0,100% 50%,84% 100%,0 100%)}
  .compare--after{left:758px;top:180px;width:142px;height:88px;background:var(--teal);color:#fff;padding:10px 10px 10px 30px;clip-path:polygon(16% 0,100% 0,100% 100%,16% 100%,0 50%)}
  .chevron{left:468px;top:290px;width:16px;height:110px}
</style>
</head>
<body>

<section class="spread spread--outside" aria-label="Außenseite">
  <div class="abs impression-box"></div>
  <div class="abs impression-card">
    <h3 class="heading">Der erste Eindruck zählt</h3>
    <p>Bei der Besichtigung entscheiden die Interessenten meist innerhalb von 30 Sekunden unterbewusst, ob ihnen die Immobilie gefällt.</p>
    <p>Die mit Home Staging vermarkteten Immobilien haben einen höheren Verkaufserlös erzielt, die Verkaufszeit reduziert und die Nachfrage gesteigert.</p>
    <p>Eine Investition in Home Staging ist ein Schlüsselerlebnis und macht sich bezahlt! Überzeugen Sie sich selbst.</p>
  </div>
  <div class="photo" role="img" aria-label="Foto: Hand stellt eine Sukkulente im Topf auf einen Holztisch" style="left:36px;top:218px;width:136px;height:115px;background:linear-gradient(160deg,#e9ecef 0%,#d8dcd8 55%,#b58a5c 100%)"></div>
  <div class="line line--dark" style="left:90px;top:347px;width:1px;height:93px"></div>
  <div class="line line--dark" style="left:178px;top:208px;width:116px;height:1px"></div>
  <div class="line" style="left:178px;top:28px;width:100px;height:1px;background:#fff"></div>
  <div class="line" style="left:278px;top:0;width:1px;height:30px;background:#fff"></div>
  <div class="abs stats">
    <div class="stat"><div class="stat__value">15 %</div><div class="stat__label">höherer<br>Verkaufserlös</div></div>
    <div class="stat"><div class="stat__value">50 %</div><div class="stat__label">reduzierte<br>Verkaufszeit</div></div>
    <div class="stat"><div class="stat__value">85 %</div><div class="stat__label">gesteigerte<br>Nachfrage</div></div>
  </div>

  <div class="photo" role="img" aria-label="Porträtfoto der Home Stagerin Karla Sonn" style="left:318px;top:0;width:165px;height:160px;background:linear-gradient(180deg,#eef0ee 0%,#d9d4cf 60%,#f4f4f4 100%)"></div>
  <div class="line" style="left:318px;top:30px;width:1px;height:390px"></div>
  <div class="line" style="left:318px;top:419px;width:282px;height:1px"></div>
  <div class="line" style="left:490px;top:30px;width:110px;height:1px"></div>
  <div class="abs brand-box" style="left:345px;top:150px;width:76px;height:98px;font-size:7px">Die<br>Raumglanz<br>Idee</div>
  <div class="abs greeting">Ich freue mich auf Ihr Projekt und ein persönliches Kennenlernen.</div>
  <div class="abs contact">
    <p><strong>Die Raumglanz Idee</strong>Home Staging &amp; Raumgestaltung</p>
    <p>Karla Sonn<br>Lindenweg 12<br>47800 Musterstadt</p>
    <p>+49 (0) 170 000 1234<br>karla@raumglanzidee.de</p>
    <p>www.raumglanzidee.de</p>
  </div>

  <div class="panel-grey" style="left:600px;top:0;width:300px;height:440px"></div>
  <div class="photo" role="img" aria-label="Foto: gestagtes Wohnzimmer mit grauem Sofa und großer Fensterfront" style="left:614px;top:18px;width:272px;height:182px;background:linear-gradient(90deg,#3c302a 0%,#8f857c 25%,#e4e4e2 55%,#b8c4a8 100%)"></div>
  <div class="abs brand-box" style="left:702px;top:18px;width:80px;height:92px;font-size:7px">Die<br>Raumglanz<br>Idee</div>
  <div class="abs cover-band">
    <div class="heading">Home Staging</div>
    <div class="sub">Erfolgreicher Immobilien verkaufen</div>
  </div>
  <div class="photo" role="img" aria-label="Foto: gestagtes Schlafzimmer mit hellem Bett, Sessel und Regal" style="left:614px;top:256px;width:272px;height:166px;background:linear-gradient(180deg,#f1f1f1 0%,#d8d6d2 55%,#cfcac4 100%)"></div>
  <div class="line" style="left:626px;top:30px;width:1px;height:380px"></div>
  <div class="line" style="left:626px;top:410px;width:262px;height:1px"></div>
  <div class="line" style="left:878px;top:30px;width:1px;height:168px"></div>
</section>

<section class="spread spread--inside" aria-label="Innenseite">
  <div class="panel-grey" style="left:0;top:0;width:300px;height:440px;background:#f3f3f3"></div>
  <div class="photo" role="img" aria-label="Foto: gestagtes Schlafzimmer mit Doppelbett, Schaukelstuhl und Spiegel" style="left:22px;top:20px;width:366px;height:288px;background:linear-gradient(180deg,#a89c98 0%,#bdb3ae 45%,#d9d2cb 75%,#c3a88a 100%)"></div>
  <div class="line" style="left:32px;top:50px;width:1px;height:60px"></div>
  <div class="line" style="left:32px;top:110px;width:250px;height:1px"></div>
  <div class="abs hero-title">
    <div class="heading">Home Staging</div>
    <div class="sub">Macht Ihre Immobilie<br>zum Blickfang</div>
  </div>
  <div class="abs definition">
    <h3 class="heading">Was ist Home Staging?</h3>
    <p>(staged = inszenieren) wird das professionelle Einrichten und Herrichten von Räumen einer Wohnung oder kompletten Immobilie zur Verkaufsförderung genannt.</p>
    <p>Ziel ist es, die perfekt hergerichtete Immobilie innerhalb kürzester Zeit zum Höchstpreis zu verkaufen.</p>
  </div>
  <div class="photo" role="img" aria-label="Foto: gestagtes Kinderzimmer mit buntem Teppich und gelben Akzenten" style="left:186px;top:295px;width:155px;height:125px;background:linear-gradient(160deg,#e8e6e3 0%,#c9c4be 50%,#3f4350 80%,#d9b75a 100%)"></div>
  <div class="line" style="left:30px;top:424px;width:240px;height:1px;background:var(--teal-dark)"></div>

  <div class="line" style="left:502px;top:0;width:1px;height:55px"></div>
  <div class="abs bestseller">
    <h3 class="heading">Ihre Immobilie wird mit mir zum Bestseller</h3>
    <p>Als professionell ausgebildete Interior Designerin / Visual Merchandiserin und Home Stagerin bin ich Ihre perfekte Ansprechpartnerin für das erfolgreiche in Szene setzen Ihrer Immobilie.</p>
    <p>Sie haben Fragen zum Thema Home Staging oder Raumgestaltung, hätten gern ein Angebot zu Ihrer Immobilie? Dann nehmen Sie gerne Kontakt mit mir auf.</p>
  </div>
  <div class="photo" role="img" aria-label="Porträtfoto der Home Stagerin Karla Sonn" style="left:482px;top:55px;width:118px;height:171px;background:linear-gradient(180deg,#e7e9e8 0%,#c8bfb6 55%,#f2f2f2 100%)"></div>
  <div class="abs nametag heading">Karla Sonn</div>
  <div class="photo" role="img" aria-label="Foto: leerer Raum vor dem Home Staging" style="left:370px;top:290px;width:100px;height:110px;background:linear-gradient(180deg,#e4dcd2 0%,#c9b8a5 60%,#6a2a2a 100%)"></div>
  <svg class="abs chevron" viewBox="0 0 16 110" aria-hidden="true"><polygon points="0,0 16,55 0,110" fill="#ffffff"/></svg>
  <div class="photo" role="img" aria-label="Foto: derselbe Raum nach dem Home Staging" style="left:484px;top:290px;width:86px;height:110px;background:linear-gradient(180deg,#f1efec 0%,#ddd6cc 60%,#c9a77f 100%)"></div>
  <div class="line" style="left:370px;top:285px;width:200px;height:1px;background:#ffffff"></div>

  <div class="panel-grey" style="left:600px;top:0;width:300px;height:440px;background:#f1f1f1"></div>
  <div class="photo" role="img" aria-label="Foto: leerer, unmöblierter Wohnraum vor dem Home Staging" style="left:700px;top:22px;width:200px;height:128px;background:linear-gradient(180deg,#e4e6e5 0%,#b7b9b7 55%,#7f817f 100%)"></div>
  <div class="line" style="left:785px;top:22px;width:1px;height:35px;background:#fff"></div>
  <div class="line" style="left:785px;top:57px;width:115px;height:1px;background:#fff"></div>
  <div class="compare compare--before">
    <h4>VORHER</h4>
    <p>Ohne Home Staging<br>3 Monate auf dem Markt,<br>15 Besichtigungen und<br>keine Kaufzusage</p>
  </div>
  <div class="photo" role="img" aria-label="Foto: gestagter Essbereich mit rundem Tisch, Rattanstühlen und Sofa nach dem Home Staging" style="left:600px;top:150px;width:273px;height:272px;background:linear-gradient(180deg,#f2f2f2 0%,#d6d6d4 45%,#8c8c8a 75%,#6f6f6d 100%)"></div>
  <div class="photo" role="img" aria-label="Foto: Fortsetzung des gestagten Essbereichs" style="left:578px;top:240px;width:22px;height:182px;background:linear-gradient(180deg,#dcdcda 0%,#8c8c8a 60%,#6f6f6d 100%)"></div>
  <div class="line line--dark" style="left:565px;top:380px;width:1px;height:60px"></div>
  <div class="line line--dark" style="left:565px;top:380px;width:120px;height:1px"></div>
  <div class="compare compare--after">
    <h4>NACHHER</h4>
    <p>Mit Home Staging<br>11 Kaufzusagen innerhalb<br>von 2 Tagen, verkauft zum<br>Wunschpreis</p>
  </div>
</section>

</body>
</html>
```